Bref créative
business card and letter head
TCW Roofing & Decks, LLC
Corporate
Dale Harrington
Project Manager / Estimator
7426-B Ferncliff
Houston, TX 77094
daleh4182@quorvix.com
Logo for TCW Roofing & Decks, LLC

```html
<!DOCTYPE html>
<html lang="en">
<head>
<meta charset="utf-8">
<title>TCW Roofing &amp; Decks, LLC — Business Card</title>
<link rel="stylesheet" href="https://fonts.googleapis.com/css2?family=Tinos:wght@400;700&display=swap">
<style>
  :root {
    --navy: #1b3563;
    --navy-deep: #142a4f;
    --silver: #c9cbce;
    --silver-light: #e4e5e7;
    --paper: #ffffff;
    --ink: #2b2b2b;
    --stage: #e9eaec;
  }
  * { box-sizing: border-box; margin: 0; padding: 0; }
  html, body {
    width: 1200px; height: 900px; overflow: hidden;
    background: var(--stage);
    font-family: "Tinos", "Times New Roman", serif;
  }
  .canvas {
    position: relative; width: 1200px; height: 900px;
  }
  .card {
    position: absolute; left: 250px; width: 700px; height: 400px;
    border-radius: 22px; overflow: hidden;
    box-shadow: 0 10px 28px rgba(0,0,0,0.18);
  }
  .card--back { top: 35px; background: var(--navy); }
  .card--front {
    top: 465px;
    background: linear-gradient(180deg, var(--paper) 0%, #f1f2f3 100%);
  }
  .brand-name {
    position: absolute;
    font-family: "Tinos", "Times New Roman", serif;
    font-weight: 700;
    line-height: 1.05;
  }
  .card--back .brand-name {
    left: 0; right: 0; top: 140px; text-align: center;
    color: var(--paper); font-size: 50px;
  }
  .card--front .brand-name {
    left: 60px; top: 110px; color: var(--navy); font-size: 44px;
  }
  .brand-name .line { display: block; }
  .brand-name .line--small { font-size: 0.56em; margin-top: 6px; }
  .swoosh { position: absolute; left: 0; bottom: 0; width: 700px; height: 400px; }
  .contact {
    position: absolute; left: 430px; top: 100px;
    color: var(--ink); font-size: 15px; line-height: 1.32;
  }
  .contact__name { font-weight: 700; font-size: 16px; }
  .contact__list { list-style: none; margin-top: 4px; }
  .contact__list li { display: flex; align-items: center; gap: 6px; }
  .contact__list svg { width: 11px; height: 11px; fill: var(--navy); flex: none; }
</style>
</head>
<body>
<main class="canvas">
  <section class="card card--back" aria-label="Card back">
    <p class="brand-name"><span class="line">TCW</span><span class="line line--small">Roofing &amp; Decks, LLC</span></p>
  </section>

  <section class="card card--front" aria-label="Card front">
    <svg class="swoosh" viewBox="0 0 700 400" aria-hidden="true">
      <path d="M0,270 C220,230 470,320 700,345 L700,400 L0,400 Z" fill="var(--silver-light)"/>
      <path d="M0,290 C230,260 470,335 700,360 L700,400 L0,400 Z" fill="var(--silver)"/>
      <path d="M0,318 C240,295 480,355 700,378" fill="none" stroke="var(--paper)" stroke-width="5"/>
      <path d="M0,328 C250,312 480,368 700,385 L700,400 L0,400 Z" fill="var(--navy)"/>
    </svg>

    <p class="brand-name"><span class="line">TCW</span><span class="line line--small">Roofing &amp; Decks, LLC</span></p>

    <div class="contact">
      <p class="contact__name">Dale Harrington</p>
      <p>Project Manager / Estimator</p>
      <p>7426-B Ferncliff</p>
      <p>Houston, TX 77094</p>
      <ul class="contact__list">
        <li><svg viewBox="0 0 12 12"><path d="M2,1 L4.5,1 L5.5,3.5 L4,4.5 C4.8,6.2 5.8,7.2 7.5,8 L8.5,6.5 L11,7.5 L11,10 C11,10.6 10.6,11 10,11 C5,11 1,7 1,2 C1,1.4 1.4,1 2,1 Z"/></svg>713-555-0142</li>
        <li><svg viewBox="0 0 12 12"><path d="M3,0.5 H9 A1,1 0 0 1 10,1.5 V10.5 A1,1 0 0 1 9,11.5 H3 A1,1 0 0 1 2,10.5 V1.5 A1,1 0 0 1 3,0.5 Z M3.5,2 V9 H8.5 V2 Z"/></svg>713-555-0187</li>
        <li><svg viewBox="0 0 12 12"><path d="M3,0.5 H9 A1,1 0 0 1 10,1.5 V10.5 A1,1 0 0 1 9,11.5 H3 A1,1 0 0 1 2,10.5 V1.5 A1,1 0 0 1 3,0.5 Z M3.5,2 V9 H8.5 V2 Z"/></svg>832-555-0163</li>
        <li><svg viewBox="0 0 12 12"><path d="M0.5,2.5 H11.5 V9.5 H0.5 Z M1.5,3.3 L6,6.5 L10.5,3.3" stroke="var(--paper)" stroke-width="0.8"/></svg>daleh4182@quorvix.com</li>
      </ul>
    </div>
  </section>
</main>
</body>
</html>
```